TILLvanta (www.tillvanta.example) needs exciting professional Business Cards

TILLvanta is an exciting new start-up targeting innovative ways to engage with retail customers at the point of sale.
Our Vision
Through applying new thinking to an old business we are reinventing selected segments of the Australian retail messaging industry, generating significant value for our customers, our suppliers, and our owners.
We operate with integrity, agility, and intelligence to doing things smarter, faster and more efficiently.
We bring deep industry expertise, deep relationships with customers and suppliers, and a will to see the old ways give way to smarter ways – this is why we win.
From this economically sustainable platform, we will examine the disruption of other market segments by further leveraging the elements that make us successful.
Our Values
With our clients, with our suppliers, with our staff, and with our owners:
# We Partner – We align the interest of all stakeholders by striving to ensure everything we do is mutually beneficial and commercially sustainable in the long term. We are clear with all our stakeholders about what our expectations are of them, and we seek clarity from them in their expectations of us.
# We Innovate – In the segments we choose to compete in, we bring fresh ideas, new business processes, the right relationships, and the right technology to ensure the supply chain is nimble, competitive, and reliable.
# We are Accountable – We say what we will do, and then do what we say.
# We Perform – We use our skills, relationships, and reputation to deliver value to our customers, suppliers, and owners.
Initially we are building our business from low-tech through printing promotional offers and retailer messages on ATM and EFTPOS receipts, but as soon as cash flow supports it we will be engaging in high-tech real-time targeted offers to the specific consumer.
I'd like the cards to reflect our values.
Please check out the web site we have just launched - it is pretty basic but it has only been up a week. We intend to sharpen it over the coming weeks, but you'll get the idea of what our core messages are.
I have recently sourced a logo from MarkForge, and have attached the source files for use.
Personal information to include:
Name: FirstName Surname
Title: Managing Director
email: first.surname@tillvanta.example
Mobile: +61-427-318-654
Generic Co Details to include:
Web: www.tillvanta.example
email: tillvanta@tillvanta.example
Fax: +61-8-7394-2816
Offices & Agents: Sydney, Melbourne, Brisbane, Adelaide, Perth
Byline: Innovation . Integrity . Service
Target Market(s)
Our customers are large corporations that have professional Point Of Sale marketing experts looking for a supplier with an edge over others in a crowded market. The buyer of our product and services is ultimately a communications expert.
They want to see distinctive competence, and an agility of thinking that will make them money through driving more consumer spending.
Industry/Entity Type
Retail
Look and feel
Each slider illustrates characteristics of the customer's brand and the style your logo design should communicate.

```html
<!DOCTYPE html>
<html lang="en">
<head>
<meta charset="utf-8">
<title>TILLvanta Business Cards</title>
<link rel="stylesheet" href="https://fonts.googleapis.com/css2?family=Arimo:wght@400;700&family=Carlito:wght@400;700&display=swap">
<style>
  :root {
    --backdrop: #363636;
    --brand-blue: #0b6ec0;
    --card-white: #ffffff;
    --tagline-grey: #a9a9a9;
    --tagline-blue: #8fb8e3;
    --text-blue: #0b6ec0;
    --divider: #0b6ec0;
  }
  * { box-sizing: border-box; margin: 0; padding: 0; }
  html, body {
    width: 1200px; height: 1000px; overflow: hidden;
    background: var(--backdrop);
  }
  .canvas {
    position: relative; width: 1200px; height: 1000px;
    font-family: "Carlito", "Calibri", sans-serif;
  }
  .card {
    position: absolute; width: 560px; height: 340px;
    border-radius: 30px; overflow: hidden;
    background: var(--card-white);
  }
  .card--front { left: 300px; top: 100px; }
  .card--back { left: 390px; top: 540px; }

  .front-panel {
    position: absolute; left: 0; top: 0; width: 100%; height: 285px;
    background: var(--brand-blue);
  }
  .wordmark {
    position: absolute;
    font-family: "Carlito", "Calibri", sans-serif; font-weight: 700;
    letter-spacing: -1px; line-height: 1;
  }
  .card--front .wordmark { left: 50px; top: 34px; font-size: 60px; color: var(--card-white); }
  .byline {
    position: absolute; font-family: "Arimo", "Arial", sans-serif;
    font-weight: 400; letter-spacing: 0;
  }
  .card--front .byline { left: 52px; top: 104px; font-size: 20px; color: var(--tagline-blue); }

  .person { position: absolute; left: 54px; top: 150px; color: var(--card-white); font-weight: 700; }
  .person__name { font-size: 22px; line-height: 26px; }
  .person__title { font-size: 20px; line-height: 24px; margin-top: 4px; }
  .person__contact { margin-top: 14px; font-size: 15px; line-height: 24px; }
  .person__contact span { display: inline-block; width: 52px; }

  .front-footer {
    position: absolute; left: 0; top: 285px; width: 100%; height: 55px;
    display: flex; align-items: center; justify-content: center;
    color: var(--text-blue); font-weight: 700; font-size: 14px; line-height: 20px;
  }
  .front-footer__divider { width: 2px; height: 38px; background: var(--divider); margin: 0 22px; }

  .card--back .wordmark { left: 54px; top: 48px; font-size: 64px; color: var(--text-blue); }
  .card--back .byline { left: 56px; top: 124px; font-size: 28px; color: var(--tagline-grey); }
  .back-web {
    position: absolute; left: 0; bottom: 14px; width: 100%; text-align: center;
    color: var(--text-blue); font-family: "Arimo", "Arial", sans-serif;
    font-weight: 700; font-size: 19px; letter-spacing: 5px;
  }
</style>
</head>
<body>
<main class="canvas">
  <section class="card card--front" aria-label="Business card front">
    <div class="front-panel">
      <div class="wordmark">TILLvanta</div>
      <p class="byline">Innovation . Integrity . Service</p>
      <div class="person">
        <p class="person__name">Mara Delcott</p>
        <p class="person__title">Managing Director</p>
        <p class="person__contact"><span>Mob.</span>+61-427-318-654<br><span>Email</span>mara.delcott@tillvanta.example</p>
      </div>
    </div>
    <div class="front-footer">
      <p>Fax:&nbsp; +61-8-7394-2816<br>www.tillvanta.example</p>
      <div class="front-footer__divider"></div>
      <p>Sydney, Melbourne,<br>Brisbane, Adelaide, Perth</p>
    </div>
  </section>

  <section class="card card--back" aria-label="Business card back">
    <div class="wordmark">TILLvanta</div>
    <p class="byline">Innovation . Integrity . Service</p>
    <p class="back-web">www.tillvanta.example</p>
  </section>
</main>
</body>
</html>
```